Personal Tax Specialists Banner

We need banner adverts for a personal tax firm. We specialise in Luxembourg, US and UK personal taxation. The banner should be modern, cool, simple and illustrated.

Banner should highlight "Personal Taxation Specialists" and the countries that we specialise in, "Luxembourg", "US" and "UK".

Target Market(s)

Individuals looking for assistance with tax return preparation.

Industry/Entity Type

Finance And Accounting

Colors

Designer to choose colors to be used in the design.

Requirements
Must have
• Output in GIF.
• The main banner size is 980 x 120 and some smaller square banners (300 x 300)
• Button to link back to website www.corvinfiling.com
Nice to have
• We would like an illustrated design if possible.

```html
<!DOCTYPE html>
<html lang="en">
<head>
<meta charset="utf-8">
<title>Corvin – Personal Taxation Specialists banners</title>
<link rel="stylesheet" href="https://fonts.googleapis.com/css2?family=Montserrat:wght@400;500;600;700;800&display=swap">
<style>
  :root{
    --board:#d6d6d6;
    --white:#ffffff;
    --maroon:#7a0d3a;
    --maroon-deep:#560726;
    --maroon-bright:#9a1450;
    --ink:#1f1f1f;
    --charcoal:#242424;
    --pale:#ececec;
    --ring:#8f8f8f;
    --grey-text:#3a3a3a;
  }
  *{margin:0;padding:0;box-sizing:border-box}
  html,body{width:1200px;height:1179px;overflow:hidden;background:var(--board)}
  body{position:relative;font-family:"Montserrat",Arial,sans-serif;color:var(--ink)}

  .section-title{position:absolute;left:0;width:1200px;text-align:center;font-size:29px;font-weight:500;letter-spacing:.3px}
  .sample-label{position:absolute;font-size:14px;font-weight:600}

  /* ---------- wide 980 x 120 banners ---------- */
  .wide{position:absolute;left:54px;width:1082px;height:133px;overflow:hidden;box-shadow:0 1px 3px rgba(0,0,0,.25)}
  .wide__bg{position:absolute;inset:0;width:100%;height:100%}
  .brand{position:absolute;display:flex;align-items:center}
  .brand__mark{border:3px solid var(--ring);border-radius:50%;flex:none}
  .brand__name{color:var(--maroon);font-weight:600;letter-spacing:.5px;line-height:1;white-space:nowrap}
  .wide .brand{left:18px;top:27px}
  .wide .brand__mark{width:78px;height:78px}
  .wide .brand__name{font-size:38px;margin-left:14px}
  .headline{position:absolute;color:var(--white);font-weight:800;text-align:center;line-height:1.14;font-size:32px;letter-spacing:.2px;white-space:nowrap}
  .markets{position:absolute;text-align:center;font-size:17px;color:var(--white);font-weight:500;white-space:nowrap}
  .markets strong{font-weight:700}
  .visit{position:absolute;display:flex;flex-direction:column;align-items:center}
  .visit__label{color:var(--white);font-size:14px;font-weight:600;letter-spacing:.3px}
  .site-btn{display:flex;align-items:center;justify-content:center;background:linear-gradient(#ffffff,#e4e4e4);border:2px solid #bdbdbd;border-radius:7px;color:var(--maroon);font-weight:500;text-decoration:none;box-shadow:0 2px 3px rgba(0,0,0,.35);white-space:nowrap}
  .wide .visit{left:812px;top:32px;width:256px}
  .wide .site-btn{width:256px;height:51px;margin-top:7px;font-size:22px}

  .wide--one .headline{left:301px;width:500px;top:14px}
  .wide--one .markets{left:296px;width:460px;top:103px}

  .wide--two .brand{left:28px;top:25px}
  .wide--two .brand__mark{width:83px;height:83px}
  .wide--two .brand__name{font-size:40px;margin-left:16px}
  .wide--two .headline{left:326px;width:500px;top:14px}
  .wide--two .markets{left:330px;width:480px;top:100px}

  .wide--three .headline{left:307px;width:500px;top:5px}
  .wide--three .markets{left:303px;width:460px;top:98px;color:var(--grey-text);font-weight:500}
  .wide--three .markets strong{color:var(--maroon)}

  /* ---------- square 300 x 300 banners ---------- */
  .square{position:absolute;top:755px;width:331px;height:331px;overflow:hidden;box-shadow:0 1px 3px rgba(0,0,0,.25)}
  .square__logo-bar{position:absolute;left:0;top:0;width:100%;height:83px;background:var(--white)}
  .square .brand{left:72px;top:14px}
  .square .brand__mark{width:58px;height:58px}
  .square .brand__name{font-size:32px;margin-left:12px}
  .square__hero{position:absolute;left:0;top:83px;width:100%;height:126px;background:linear-gradient(160deg,var(--maroon-bright),var(--maroon) 45%,var(--maroon-deep))}
  .square .headline{left:0;width:100%;top:95px;font-size:34px;line-height:1.0;letter-spacing:0}
  .square__markets{position:absolute;left:0;top:209px;width:100%;height:54px;text-align:center;font-size:17px;line-height:1.4;padding-top:3px;white-space:nowrap}
  .square__markets strong{display:block;font-weight:700;font-size:17px}
  .square__foot{position:absolute;left:0;top:263px;width:100%;height:68px;background:var(--charcoal)}
  .square .visit{flex-direction:row;left:22px;top:276px}
  .square .visit__label{font-size:13px;width:83px}
  .square .site-btn{width:203px;height:40px;font-size:16px}

  .square--one{left:50px}
  .square--one .square__markets{background:var(--pale);color:var(--grey-text)}
  .square--two{left:426px}
  .square--two .square__markets{background:var(--charcoal);color:var(--white)}
  .square--two .square__foot{background:var(--maroon)}
  .square--three{left:802px}
  .square--three .square__hero{height:180px}
  .square--three .headline{top:92px}
  .square--three .square__markets{color:var(--white);top:205px}
</style>
</head>
<body>

<h1 class="section-title" style="top:55px">banner size is 980 x 120</h1>

<div class="wide wide--one" style="top:119px">
  <svg class="wide__bg" viewBox="0 0 1082 133" preserveAspectRatio="none">
    <defs>
      <linearGradient id="wineOne" x1="0" y1="0" x2="1" y2="1">
        <stop offset="0" stop-color="#8e1148"/><stop offset="1" stop-color="#5a0828"/>
      </linearGradient>
    </defs>
    <rect width="1082" height="133" fill="#232323"/>
    <g role="img" aria-label="City bridge photograph tinted in wine red">
      <polygon points="336,0 811,0 760,133 270,133" fill="url(#wineOne)"/>
    </g>
    <polygon points="811,0 821,0 770,133 760,133" fill="#b9b9b9"/>
    <polygon points="0,0 336,0 270,133 0,133" fill="#ffffff"/>
    <polygon points="336,0 344,0 278,133 270,133" fill="#d9d9d9"/>
  </svg>
  <div class="brand"><span class="brand__mark"></span><span class="brand__name">CORVIN</span></div>
  <h2 class="headline">PERSONAL TAXATION<br>SPECIALISTS</h2>
  <p class="markets">We specialize in <strong>Luxembourg, US and UK</strong></p>
  <div class="visit"><span class="visit__label">VISIT US AT</span><a class="site-btn" href="#">www.corvinfiling.com</a></div>
</div>
<span class="sample-label" style="left:56px;top:262px">Samplle 1</span>

<div class="wide wide--two" style="top:299px">
  <svg class="wide__bg" viewBox="0 0 1082 133" preserveAspectRatio="none">
    <defs>
      <linearGradient id="wineTwo" x1="0" y1="0" x2="1" y2="1">
        <stop offset="0" stop-color="#6a0a30"/><stop offset=".6" stop-color="#8a1250"/><stop offset="1" stop-color="#a2124a"/>
      </linearGradient>
    </defs>
    <g role="img" aria-label="Luxembourg city skyline and bridge photograph tinted in magenta">
      <rect width="1082" height="133" fill="url(#wineTwo)"/>
    </g>
    <polygon points="0,0 336,0 356,66 336,133 0,133" fill="#e6c3d3"/>
    <polygon points="0,0 314,0 334,66 314,133 0,133" fill="#ffffff"/>
  </svg>
  <div class="brand"><span class="brand__mark"></span><span class="brand__name">CORVIN</span></div>
  <h2 class="headline">PERSONAL TAXATION<br>SPECIALISTS</h2>
  <p class="markets">We specialize in, <strong>Luxembourg, US and UK</strong></p>
  <div class="visit"><span class="visit__label">VISIT US AT</span><a class="site-btn" href="#">www.corvinfiling.com</a></div>
</div>
<span class="sample-label" style="left:55px;top:446px">Samplle 2</span>

<div class="wide wide--three" style="top:482px">
  <svg class="wide__bg" viewBox="0 0 1082 133" preserveAspectRatio="none">
    <defs>
      <linearGradient id="nightThree" x1="0" y1="0" x2="0" y2="1">
        <stop offset="0" stop-color="#3b3b40"/><stop offset=".5" stop-color="#2a2b25"/><stop offset="1" stop-color="#1c1e17"/>
      </linearGradient>
    </defs>
    <g role="img" aria-label="Night photograph of a city viaduct">
      <rect width="1082" height="133" fill="url(#nightThree)"/>
    </g>
    <polygon points="0,0 330,0 270,133 0,133" fill="#ffffff"/>
    <polygon points="330,0 806,0 780,88 290,88" fill="#7a0d3a"/>
    <polygon points="290,88 780,88 765,133 270,133" fill="#ececec"/>
  </svg>
  <div class="brand"><span class="brand__mark"></span><span class="brand__name">CORVIN</span></div>
  <h2 class="headline">PERSONAL TAXATION<br>SPECIALISTS</h2>
  <p class="markets">We specialize in, <strong>Luxembourg, US and UK</strong></p>
  <div class="visit"><span class="visit__label">VISIT US AT</span><a class="site-btn" href="#">www.corvinfiling.com</a></div>
</div>
<span class="sample-label" style="left:57px;top:629px">Samplle 3</span>

<h1 class="section-title" style="top:668px">banner size is 300 x 300</h1>

<div class="square square--one">
  <div class="square__logo-bar"></div>
  <div class="brand"><span class="brand__mark"></span><span class="brand__name">CORVIN</span></div>
  <div class="square__hero" role="img" aria-label="City skyline photograph tinted in wine red"></div>
  <h2 class="headline">PERSONAL<br>TAXATION<br>SPECIALISTS</h2>
  <p class="square__markets">We specialize in<strong>LUXEMBOURG, US AND UK</strong></p>
  <div class="square__foot"></div>
  <div class="visit"><span class="visit__label">VISIT US AT</span><a class="site-btn" href="#">www.corvinfiling.com</a></div>
</div>

<div class="square square--two">
  <div class="square__logo-bar"></div>
  <div class="brand"><span class="brand__mark"></span><span class="brand__name">CORVIN</span></div>
  <div class="square__hero" role="img" aria-label="City skyline photograph tinted in wine red"></div>
  <h2 class="headline">PERSONAL<br>TAXATION<br>SPECIALISTS</h2>
  <p class="square__markets">We specialize in<strong>LUXEMBOURG, US AND UK</strong></p>
  <div class="square__foot"></div>
  <div class="visit"><span class="visit__label">VISIT US AT</span><a class="site-btn" href="#">www.corvinfiling.com</a></div>
</div>

<div class="square square--three">
  <div class="square__logo-bar"></div>
  <div class="brand"><span class="brand__mark"></span><span class="brand__name">CORVIN</span></div>
  <div class="square__hero" role="img" aria-label="City bridge photograph tinted in wine red"></div>
  <h2 class="headline">PERSONAL<br>TAXATION<br>SPECIALISTS</h2>
  <p class="square__markets">We specialize in<strong>LUXEMBOURG, US AND UK</strong></p>
  <div class="square__foot"></div>
  <div class="visit"><span class="visit__label">VISIT US AT</span><a class="site-btn" href="#">www.corvinfiling.com</a></div>
</div>

<span class="sample-label" style="left:182px;top:1111px">Samplle 1</span>
<span class="sample-label" style="left:560px;top:1111px">Samplle 2</span>
<span class="sample-label" style="left:933px;top:1111px">Samplle 3</span>

</body>
</html>
```